依頼詳細
主にWEBサイトで販売する薬品希釈用精製水のラベルのデザイン作成依頼です。
ラベルはペットボトルにシュリンク包装します。

用途は、薬品の希釈やエタノールや塩素を希釈してアルコール消毒液や除菌剤を作る時に
使用されます。参考画像を添付します。

デザインの詳細は添付のエクセルをご参照ください。
デザインは正面の1面のみとなります。

WEB上のサムネイルで最も目に付くところで、特に「商品名」「イラスト」「特長」で
用途を一目で伝えるデザイン性を重要視します。

目的に沿ったデザインであれば、色やフォントなどは問いません。
商品名・イラスト・特長・社名・容量の配置も特に決まりはありません。

WEBに掲載した際に用途がわかりやすく、手にとっても見やすいデザインを希望します。

サイズも添付のエクセルに記載していますので、そのサイズ内での作成をお願い致します。
ペットボトルの中央にくぼみがありますので、それを利用した(上部と下部に分けた)デザインでも構いませんし、ラベルサイズ全体を利用したデザインでも構いません。

今回のサイズとは別に3種類のサイズ違い製品があります。
デザイン採用後に、デザインはそのままでリサイズのみ行っていただく作業もございます。

競合品や用途の参考となる画像も添付しますので参照とされてください。

どうぞよろしくお願いいたします。
記載項目
添付資料をご参照ください。
希望イメージ
シンプル 複雑
単色 カラフル
暗い 明るい
日常 高級
遊び心 厳粛
未来的 伝統的
女性的 男性的
希望する色
青系、水色系、紫系
納品ファイル
• 高解像度JPG (.jpg)
• イラストレーター形式 (.ai)
補足説明

商品に合ったご提案でした。

ご提案ありがとうございました。
またの機会がございましたらよろしくお願いいたします。

```html
<!DOCTYPE html>
<html lang="ja">
<head>
<meta charset="utf-8">
<title>精製水 ラベル</title>
<link rel="stylesheet" href="https://fonts.googleapis.com/css2?family=Kosugi+Maru&family=Noto+Sans+JP:wght@400;500&display=swap">
<style>
  :root {
    --sky-top: #f2f8fd;
    --sky-bottom: #d6eaf8;
    --brand: #2d6db4;
    --title: #ffffff;
    --title-shade: #6aa9dc;
    --wave-light: #8cc7ef;
    --wave-mid: #4aa3e4;
    --body-top: #3f9be0;
    --body-bottom: #1f78cc;
    --footer: #1e5fa9;
    --white: #ffffff;
    --rule: rgba(255,255,255,0.6);
  }
  html, body { margin: 0; padding: 0; overflow: hidden; }
  .label {
    position: relative;
    width: 1200px; height: 2928px;
    overflow: hidden;
    background: linear-gradient(180deg, var(--body-top) 1320px, var(--body-bottom) 2760px);
    font-family: "Noto Sans JP", sans-serif;
    color: var(--white);
  }
  .top-scene { position: absolute; left: 0; top: 0; width: 1200px; height: 1400px; }
  .usage-band {
    position: absolute; left: 200px; top: 32px; width: 800px; height: 96px;
    background: var(--brand);
    display: flex; align-items: center; justify-content: center;
    font-size: 56px; font-weight: 500; letter-spacing: 2px;
  }
  .product-name {
    position: absolute; left: 0; right: 0; top: 330px; margin: 0;
    text-align: center;
    font-family: "Kosugi Maru", sans-serif;
    font-weight: 400; font-size: 250px; letter-spacing: 30px;
    line-height: 290px;
    color: var(--title);
    text-shadow: 0 0 6px var(--title-shade), 4px 6px 0 var(--title-shade);
  }
  .feature {
    position: absolute; left: 100px; width: 1000px;
    text-align: center;
  }
  .feature-lead { font-size: 40px; font-weight: 400; line-height: 60px; }
  .feature-main { font-size: 64px; font-weight: 500; line-height: 92px; }
  .feature-main small { font-size: 44px; }
  .feature-1 { top: 1510px; }
  .feature-2 { top: 1800px; }
  .feature-3 { top: 2060px; }
  .feature-4 { top: 2320px; }
  .rule {
    position: absolute; left: 100px; width: 1000px; height: 0;
    border-top: 3px solid var(--rule);
  }
  .rule-1 { top: 1740px; }
  .rule-2 { top: 2004px; }
  .rule-3 { top: 2262px; }
  .volume {
    position: absolute; left: 448px; top: 2630px; width: 304px; height: 76px;
    border: 3px solid var(--white); box-sizing: border-box;
    display: flex; align-items: center; justify-content: center;
    font-size: 40px;
  }
  .company {
    position: absolute; left: 0; bottom: 0; width: 1200px; height: 168px;
    background: var(--footer);
    display: flex; align-items: center; justify-content: center;
    font-size: 64px; font-weight: 500; letter-spacing: 4px;
  }
</style>
</head>
<body>
<div class="label">
  <svg class="top-scene" viewBox="0 0 1200 1400" xmlns="http://www.w3.org/2000/svg">
    <defs>
      <linearGradient id="sky" x1="0" y1="0" x2="0" y2="1">
        <stop offset="0" stop-color="#f2f8fd"/>
        <stop offset="1" stop-color="#d6eaf8"/>
      </linearGradient>
    </defs>
    <rect width="1200" height="1400" fill="url(#sky)"/>
    <path d="M0 1120 C260 1060 440 1160 680 1100 C880 1040 1040 820 1200 600 L1200 1400 L0 1400 Z" fill="var(--wave-light)"/>
    <path d="M0 1220 C260 1140 480 1250 720 1200 C920 1150 1060 1040 1200 900 L1200 1400 L0 1400 Z" fill="var(--wave-mid)"/>
    <path d="M0 1320 C300 1260 560 1350 820 1310 C980 1285 1100 1240 1200 1200 L1200 1400 L0 1400 Z" fill="var(--body-top)"/>
    <rect x="240" y="740" width="900" height="420" rx="24" fill="#c6e1f5" opacity="0.85" role="img" aria-label="洗浄瓶とビーカーが並び、右側から水しぶきが立ち上がるイラスト"/>
  </svg>

  <div class="usage-band">薬品・アルコール希釈用</div>
  <h1 class="product-name">精製水</h1>

  <div class="feature feature-1">
    <div class="feature-lead">薬品等の希釈に最適な極めて不純物の少ない</div>
    <div class="feature-main">高純度精製水</div>
  </div>
  <div class="rule rule-1"></div>
  <div class="feature feature-2">
    <div class="feature-lead">日本産業規格「JIS-K0557」における</div>
    <div class="feature-main">A2クラス相当品</div>
  </div>
  <div class="rule rule-2"></div>
  <div class="feature feature-3">
    <div class="feature-lead">薬品本来の性能を損なわず</div>
    <div class="feature-main">安全な調整・調合<small>が可能</small></div>
  </div>
  <div class="rule rule-3"></div>
  <div class="feature feature-4">
    <div class="feature-lead">工業薬品の希釈やアルコール消毒液</div>
    <div class="feature-main">除菌液の作製に</div>
  </div>

  <div class="volume">容量：330ml</div>
  <div class="company">ミナト化学株式会社</div>
</div>
</body>
</html>
```